velto GmbH - Business Cards etc.
velto GmbH
Project: velto GmbH - Business Cards etc.
velto GmbH - Business Cards etc. - Retailers
Creative Brief
Professional
Konrad Wieslauer
CEO
Gisela Brandtner Str. 23 76139 Karlsruhe
k.wieslauer@veltohouse.com
www.veltohouse.com
The business card MUST have the following format: 85 x 55mm PLUS a 3mm addition on every side. This means the image size must be 91 x 61mm
Concepts
Business Cards/Letterhead/ Envelopes/Notepads/Tshirt/labels for tiny tall crate
Business cards and company letter head for Osaka Dine Court
konrad konrad
I don't have a logo unfortunately. I've started a logo design project but it was not successful. I really need biz cards now and want to find a logo later. The logo on the biz cards is not so important in this case.
I wonder why there are so few contributions to this project? What's missing? How can I help?

```html
<!DOCTYPE html>
<html lang="de">
<head>
<meta charset="utf-8">
<title>velto GmbH – Business Card</title>
<link rel="stylesheet" href="https://fonts.googleapis.com/css2?family=Roboto+Condensed:wght@400;700&family=Roboto:wght@300;700;900&display=swap">
<style>
  :root {
    --page: #f4f4f4;
    --card: #ffffff;
    --card-edge: #d6d6d6;
    --band: #1c4f5e;
    --band-text: #ffffff;
    --ink: #1a1a1a;
    --ink-soft: #333333;
  }
  * { box-sizing: border-box; margin: 0; padding: 0; }
  html, body {
    width: 1200px;
    height: 871px;
    overflow: hidden;
    background: var(--page);
  }
  .business-card {
    position: absolute;
    left: 365px;
    top: 40px;
    width: 540px;
    height: 785px;
    background: var(--card);
    border: 1px solid var(--card-edge);
  }
  .brand-band {
    height: 100px;
    background: var(--band);
    padding: 18px 0 0 30px;
  }
  .brand-name {
    color: var(--band-text);
    font-family: "Roboto", sans-serif;
    font-weight: 900;
    font-size: 72px;
    line-height: 1;
    letter-spacing: -3px;
  }
  .brand-name .legal-form {
    font-size: 22px;
    letter-spacing: 0;
    vertical-align: 38px;
    margin-left: 6px;
  }
  .contact-block {
    padding: 38px 0 0 30px;
    font-family: "Roboto Condensed", sans-serif;
    font-weight: 400;
    font-size: 26px;
    line-height: 35px;
    color: var(--ink-soft);
  }
  .holder {
    position: absolute;
    left: 0;
    right: 0;
    top: 610px;
    text-align: center;
    color: var(--ink);
  }
  .holder-name {
    font-family: "Roboto", sans-serif;
    font-weight: 300;
    font-size: 54px;
    line-height: 1.1;
    letter-spacing: -0.5px;
  }
  .holder-role {
    margin-top: 6px;
    font-family: "Roboto", sans-serif;
    font-weight: 700;
    font-size: 22px;
  }
</style>
</head>
<body>
  <article class="business-card">
    <header class="brand-band">
      <div class="brand-name">velto<span class="legal-form">GmbH</span></div>
    </header>
    <address class="contact-block" style="font-style: normal;">
      <div class="contact-line">Gisela Brandtner Str. 23</div>
      <div class="contact-line">76139 KarlsruhePhone +49 (0) 721 480 3316</div>
      <div class="contact-line">Fax +49 (0) 721 480 3317</div>
      <div class="contact-line">Email: k.wieslauer@veltohouse.com</div>
      <div class="contact-line">www.veltohouse.com</div>
    </address>
    <section class="holder">
      <div class="holder-name">Konrad Wieslauer</div>
      <div class="holder-role">CEO</div>
    </section>
  </article>
</body>
</html>
```